New Business Cards for Torvin Group

We need a new Business Card to compliment our new logo. We are a vibrant design, manufacture and install business providing recreation areas, public parks and Municipal spaces. We want business cards that are classy, modern and clean.

We have recently changed our logo, and are celebrating our 40th anniversary. We want business cards with a new modern design to reflect our status.

Target Market(s)

Customers

Contact Information for Business Card

We need all the details of our 3 offices as per the business card attached. Please disregard the old logo on the business card, the other three files show our new logo.

Requirements
Must have
• All info as per attached business card but with new logo.
Nice to have

```html
<!DOCTYPE html>
<html lang="en">
<head>
<meta charset="utf-8">
<title>Torvin Group – Business Card</title>
<link href="https://fonts.googleapis.com/css2?family=Montserrat:wght@400;500;700;800&display=swap" rel="stylesheet">
<style>
  :root {
    --indigo: #24197c;
    --indigo-light: #3a30a0;
    --red: #e8303c;
    --white: #ffffff;
    --backdrop: #e4e3ea;
  }
  * { margin: 0; padding: 0; box-sizing: border-box; }
  html, body {
    width: 1200px; height: 900px; overflow: hidden;
    background: var(--backdrop);
    font-family: "Montserrat", sans-serif;
  }
  .card {
    position: absolute; left: 120px; top: 176px;
    width: 960px; height: 548px;
    background: var(--indigo);
    overflow: hidden;
    box-shadow: 0 12px 30px rgba(30, 20, 80, 0.25);
  }
  .world-map {
    position: absolute; left: 300px; top: 60px; width: 620px; height: 330px;
    background: radial-gradient(ellipse at center, rgba(80, 70, 190, 0.55) 0%, rgba(60, 50, 170, 0.25) 55%, rgba(36, 25, 124, 0) 75%);
  }
  .card-shapes { position: absolute; inset: 0; }
  .brand {
    position: absolute; left: 62px; top: 150px;
    display: flex; align-items: center; gap: 16px;
  }
  .brand-dot { width: 34px; height: 34px; border-radius: 50%; background: var(--red); }
  .brand-name {
    color: var(--white); font-weight: 800; font-size: 44px; letter-spacing: 1px;
  }
  .holder { position: absolute; left: 96px; top: 362px; }
  .holder-name { color: var(--white); font-weight: 800; font-size: 42px; }
  .holder-title { color: var(--indigo); font-weight: 700; font-size: 22px; margin-top: 2px; padding-left: 50px; }
  .website {
    position: absolute; left: 430px; top: 496px;
    color: var(--white); font-size: 13px; font-weight: 500;
  }
  .offices { position: absolute; left: 580px; top: 48px; width: 360px; }
  .office { margin-bottom: 24px; }
  .office-title { color: var(--white); font-weight: 700; font-size: 15px; margin-bottom: 4px; }
  .contact-line {
    display: flex; align-items: center; gap: 8px;
    color: var(--white); font-size: 13.5px; line-height: 19px;
  }
  .contact-line svg { width: 12px; height: 12px; flex: none; fill: var(--red); }
</style>
</head>
<body>
<article class="card">
  <div class="world-map" role="img" aria-label="Faint world map in the background"></div>

  <svg class="card-shapes" viewBox="0 0 960 548" aria-hidden="true">
    <polygon points="0,300 500,300 690,470 0,470" fill="var(--red)"/>
    <polygon points="556,298 596,298 782,470 742,470" fill="var(--red)"/>
    <rect x="0" y="470" width="960" height="10" fill="var(--indigo)"/>
    <rect x="0" y="480" width="960" height="68" fill="var(--red)"/>
    <rect x="0" y="522" width="420" height="7" fill="var(--indigo)"/>
  </svg>

  <div class="brand">
    <span class="brand-dot"></span>
    <span class="brand-name">TORVIN GROUP</span>
  </div>

  <div class="holder">
    <h1 class="holder-name">Marek Dunholt</h1>
    <p class="holder-title">Managing Partner</p>
  </div>

  <p class="website">www.torvingroup.com</p>

  <section class="offices">
    <div class="office">
      <h2 class="office-title">Head Office</h2>
      <p class="contact-line"><svg viewBox="0 0 12 12"><path d="M6 0a4 4 0 0 0-4 4c0 3 4 8 4 8s4-5 4-8a4 4 0 0 0-4-4zm0 5.5A1.5 1.5 0 1 1 6 2.5a1.5 1.5 0 0 1 0 3z"/></svg>P.O. Box: 31408 Abu Dhabi, U.A.E.</p>
      <p class="contact-line"><svg viewBox="0 0 12 12"><path d="M2 0h3l1 3-2 1a7 7 0 0 0 4 4l1-2 3 1v3a2 2 0 0 1-2 2A10 10 0 0 1 0 2a2 2 0 0 1 2-2z"/></svg>Tel No: +971 (0)2 5280317</p>
      <p class="contact-line"><svg viewBox="0 0 12 12"><rect x="3" y="0" width="6" height="4"/><rect x="0" y="4" width="12" height="6" rx="1"/><rect x="3" y="8" width="6" height="4"/></svg>Fax No: +971 (0)2 5280318</p>
      <p class="contact-line"><svg viewBox="0 0 12 12"><path d="M0 2h12v8H0zM1 3l5 4 5-4" stroke="var(--indigo)" stroke-width="1"/></svg>Email: sales@torvingroup.com</p>
    </div>
    <div class="office">
      <h2 class="office-title">Dubai Office</h2>
      <p class="contact-line"><svg viewBox="0 0 12 12"><path d="M6 0a4 4 0 0 0-4 4c0 3 4 8 4 8s4-5 4-8a4 4 0 0 0-4-4zm0 5.5A1.5 1.5 0 1 1 6 2.5a1.5 1.5 0 0 1 0 3z"/></svg>P.O. Box: 472210 Dubai, U.A.E.</p>
      <p class="contact-line"><svg viewBox="0 0 12 12"><path d="M2 0h3l1 3-2 1a7 7 0 0 0 4 4l1-2 3 1v3a2 2 0 0 1-2 2A10 10 0 0 1 0 2a2 2 0 0 1 2-2z"/></svg>Tel No: +971 (0)4 3906624</p>
      <p class="contact-line"><svg viewBox="0 0 12 12"><rect x="3" y="0" width="6" height="4"/><rect x="0" y="4" width="12" height="6" rx="1"/><rect x="3" y="8" width="6" height="4"/></svg>Fax No: +971 (0)4 3906625</p>
      <p class="contact-line"><svg viewBox="0 0 12 12"><path d="M0 2h12v8H0zM1 3l5 4 5-4" stroke="var(--indigo)" stroke-width="1"/></svg>Email: sales@torvingroup.com</p>
    </div>
    <div class="office">
      <h2 class="office-title">Qatar Office</h2>
      <p class="contact-line"><svg viewBox="0 0 12 12"><path d="M6 0a4 4 0 0 0-4 4c0 3 4 8 4 8s4-5 4-8a4 4 0 0 0-4-4zm0 5.5A1.5 1.5 0 1 1 6 2.5a1.5 1.5 0 0 1 0 3z"/></svg>P.O. Box: 20873 Doha, Qatar</p>
      <p class="contact-line"><svg viewBox="0 0 12 12"><path d="M2 0h3l1 3-2 1a7 7 0 0 0 4 4l1-2 3 1v3a2 2 0 0 1-2 2A10 10 0 0 1 0 2a2 2 0 0 1 2-2z"/></svg>Tel No: +974 44710382</p>
      <p class="contact-line"><svg viewBox="0 0 12 12"><rect x="3" y="0" width="6" height="4"/><rect x="0" y="4" width="12" height="6" rx="1"/><rect x="3" y="8" width="6" height="4"/></svg>Fax No: +974 44710390</p>
      <p class="contact-line"><svg viewBox="0 0 12 12"><path d="M0 2h12v8H0zM1 3l5 4 5-4" stroke="var(--indigo)" stroke-width="1"/></svg>Email: sales@torvingroup.com</p>
    </div>
  </section>
</article>
</body>
</html>
```